"The Plumeworks" nails, eyelash extensions and hair extensions. Need an eye catching design for bu

Need an eye catching design focusing on eyelash extensions, nail extensions and hair extensions. I like the colour green, black, glitter, pink?! need the design to be innovative and 'POP'. I'd like more emphasis on lashes and nails.
I'd like the business name and my phone number on the front of card.
Would really like something different and unique.
"The Plumeworks"
Nails, Eyelash & Hair Extensions
Mira
0417265903

Target Market(s)

20-40

Industry/Entity Type

Beauty Salon

Contact Information for Business Card

Id like my business name, My name and phone number on the front of card
"The Plumeworks".
Mira.
0417265903.
Id like some catchy design involving long lashes with possibly glitter, long hair and nails. Id like the lashes to be the first thing you see at first glance. I'm open to your creative flair. Just need the business card design to 'POP'! I like the colours green, black, pink, silver or gold glitter. wether it's pop art, 3d drawn pictures, isolated pics of lash, nails or hair, card design could be in black and white with isolated colours added..i'm open to your creative flair. use a font which stands out and easy to read.
(The back of the card will be used for writing appointment times.)

Font styles to use
Serif

Colors
6b449b
e667a6
25b39d

Requirements
Must have
• Long lashes, hair, nails.
• one sided
Nice to have
• bright catchy colours, innovative, uniqueness

```html
<!DOCTYPE html>
<html lang="en">
<head>
<meta charset="utf-8">
<title>The Plumeworks – Business Card</title>
<link rel="stylesheet" href="https://fonts.googleapis.com/css2?family=Noto+Serif:wght@400&family=Open+Sans:wght@300&display=swap">
<style>
  :root {
    --page-bg: #e8e5e0;
    --card-grey: #8f8f8f;
    --card-grey-light: #9d9d9d;
    --band-black: #232323;
    --accent-teal: #25b39d;
    --accent-pink: #e667a6;
    --ink: #262626;
    --lash-dark: #1a1a1a;
  }
  * { margin: 0; padding: 0; box-sizing: border-box; }
  html, body {
    width: 1200px;
    height: 1023px;
    overflow: hidden;
    background: var(--page-bg);
  }
  .stage {
    width: 1200px;
    height: 1023px;
    display: flex;
    align-items: center;
    justify-content: center;
  }
  .business-card {
    position: relative;
    width: 1050px;
    height: 600px;
    overflow: hidden;
    background: linear-gradient(160deg, var(--card-grey-light), var(--card-grey));
    box-shadow: 0 10px 30px rgba(0,0,0,0.18);
  }
  .lash-visual {
    position: absolute;
    left: 380px;
    top: 250px;
    width: 300px;
    height: 330px;
    background: radial-gradient(ellipse at 90% 20%, var(--lash-dark) 0%, rgba(40,40,40,0.85) 30%, rgba(120,120,120,0.35) 65%, rgba(143,143,143,0) 80%);
  }
  .stripe-panel {
    position: absolute;
    top: 0;
    right: 0;
    width: 370px;
    height: 600px;
  }
  .card-text {
    position: absolute;
    left: 130px;
    top: 92px;
    color: var(--ink);
  }
  .business-name {
    font-family: "Noto Serif", serif;
    font-weight: 400;
    font-size: 44px;
    line-height: 1;
  }
  .services {
    font-family: "Open Sans", sans-serif;
    font-weight: 300;
    font-size: 25px;
    margin-top: 14px;
  }
  .owner-name {
    font-family: "Noto Serif", serif;
    font-size: 40px;
    line-height: 1;
    margin-top: 42px;
  }
  .phone {
    font-family: "Open Sans", sans-serif;
    font-weight: 300;
    font-size: 25px;
    letter-spacing: 1px;
    margin-top: 10px;
  }
</style>
</head>
<body>
<main class="stage">
  <section class="business-card">
    <div class="lash-visual" role="img" aria-label="Close-up photograph of long curled black eyelashes"></div>

    <svg class="stripe-panel" viewBox="0 0 370 600" aria-hidden="true">
      <rect class="band-black" x="0" y="0" width="370" height="600" fill="var(--band-black)"/>
      <polygon class="band-teal" fill="var(--accent-teal)"
        points="245,0 252,0 250,25 254,50 249,75 253,100 250,125 254,150 249,175 253,200 250,225 254,250 249,275 253,300 250,325 254,350 249,375 253,400 250,425 254,450 249,475 253,500 250,525 254,550 249,575 252,600
                275,600 280,575 276,550 281,525 277,500 281,475 276,450 280,425 277,400 281,375 276,350 280,325 277,300 281,275 276,250 280,225 277,200 281,175 276,150 280,125 277,100 281,75 276,50 280,25 277,0"/>
      <rect class="band-pink" x="298" y="0" width="72" height="600" fill="var(--accent-pink)"/>
    </svg>

    <div class="card-text">
      <h1 class="business-name">The Plumeworks</h1>
      <p class="services">Nails, Eyelash &amp; Hair Extensions</p>
      <p class="owner-name">Mira</p>
      <p class="phone">04 17 26 59 03</p>
    </div>
  </section>
</main>
</body>
</html>
```